Clean, Fresh Business Card Design Needed

We need a business card design for a new business we have taken over called "Bonders and Fixers". We got a logo through this website which i have attached. We are wanting something that is vibrant but clean and fresh. Our business mainly sells glue. Maybe a cool design/slogan on the back? Modern, sleek.

Industry/Entity Type

Business

Contact Information for Business Card

Name: Derek Tamsin, Managing Director. Address: 164 Kowhai Lane, Kereru Bay 3175, Phone: 07 549 2361 Mobile: 021 634 915 Fax: 07 549 2874 Email: bond.fix@mailvo.co.nz, Web: www.tackbondpro.co.nz

Font styles to use
Serif

Requirements
Must have
• All business card details, logo.
Nice to have
• Design, slogan on back of card

```html
<!DOCTYPE html>
<html lang="en">
<head>
<meta charset="utf-8">
<title>Bonders and Fixers – Business Card</title>
<link rel="stylesheet" href="https://fonts.googleapis.com/css2?family=Cinzel:wght@400;600&family=Lato:wght@400&family=Questrial&display=swap">
<style>
  :root {
    --stage: #2b2b2d;
    --navy: #2a3a8c;
    --navy-deep: #1c2660;
    --ink: #151515;
    --paper: #ffffff;
    --paper-shade: #eeeeee;
  }
  * { margin: 0; padding: 0; box-sizing: border-box; }
  html, body { width: 1200px; height: 997px; overflow: hidden; }
  body { background: var(--stage); position: relative; }

  .card {
    position: absolute;
    width: 560px;
    height: 320px;
    box-shadow: 0 18px 40px rgba(0,0,0,0.45);
    overflow: hidden;
  }

  /* Back of card */
  .card-back {
    left: 70px; top: 110px;
    background: var(--navy);
  }
  .card-back .brand {
    position: absolute; left: 60px; top: 92px;
    display: flex; align-items: center; gap: 18px;
  }
  .card-back .brand-square {
    width: 82px; height: 82px; border-radius: 12px;
    background: var(--paper);
  }
  .card-back .brand-name {
    font-family: "Cinzel", serif; font-weight: 400;
    font-size: 36px; line-height: 1.05; color: var(--navy-deep);
    letter-spacing: 1px;
  }
  .card-back .slogan {
    position: absolute; left: 160px; top: 196px; width: 300px;
    font-family: "Lato", sans-serif; font-size: 17px; line-height: 1.35;
    color: var(--paper);
  }
  .card-back .website {
    position: absolute; left: 160px; top: 268px;
    font-family: "Questrial", sans-serif; font-size: 13px;
    letter-spacing: 4px; color: var(--navy-deep);
  }

  /* Front of card */
  .card-front {
    left: 570px; top: 540px;
    background: linear-gradient(135deg, var(--paper) 0%, var(--paper-shade) 100%);
  }
  .card-front .person {
    position: absolute; left: 95px; top: 48px;
  }
  .card-front .person-name {
    font-family: "Cinzel", serif; font-weight: 600; font-size: 18px;
    color: var(--navy); letter-spacing: 1px;
  }
  .card-front .person-role {
    font-family: "Questrial", sans-serif; font-size: 10px;
    color: var(--ink); letter-spacing: 1px; text-transform: uppercase;
  }
  .card-front .brand {
    position: absolute; right: 40px; top: 38px;
    display: flex; flex-direction: column; align-items: flex-end; gap: 10px;
  }
  .card-front .brand-square {
    width: 66px; height: 66px; border-radius: 8px;
    background: var(--navy); margin-right: 90px;
  }
  .card-front .brand-name {
    font-family: "Cinzel", serif; font-weight: 400; font-size: 30px;
    line-height: 1.05; color: var(--ink); text-align: right;
  }
  .icon-tab {
    position: absolute; left: 30px; top: 150px; width: 52px; height: 150px;
    background: var(--navy); border-radius: 12px 0 0 0;
    display: flex; flex-direction: column; align-items: center;
    justify-content: space-around; padding: 8px 0;
  }
  .icon-tab svg { width: 16px; height: 16px; fill: var(--paper); }
  .contact-list {
    position: absolute; left: 98px; top: 155px; list-style: none;
    font-family: "Questrial", sans-serif; font-size: 13.5px; color: var(--ink);
  }
  .contact-list li { height: 28px; line-height: 28px; }
  .card-front .edge-bands {
    position: absolute; left: 0; bottom: 0; width: 560px; height: 80px;
  }
</style>
</head>
<body>

  <section class="card card-back" aria-label="Back of business card">
    <div class="brand">
      <div class="brand-square"></div>
      <div class="brand-name">Bonders<br>and Fixers</div>
    </div>
    <p class="slogan">Glues, Adhesives &amp; Sealants From Industrial Strength Through To Craft Glues</p>
    <p class="website">www.tackbondpro.co.nz</p>
  </section>

  <section class="card card-front" aria-label="Front of business card">
    <div class="person">
      <p class="person-name">Derek Tamsin</p>
      <p class="person-role">Managing Director</p>
    </div>

    <div class="brand">
      <div class="brand-square"></div>
      <div class="brand-name">Bonders<br>and Fixers</div>
    </div>

    <div class="icon-tab">
      <svg viewBox="0 0 16 16" aria-label="Phone"><path d="M2 5c0-2 2-3 6-3s6 1 6 3v1h-3V5H5v1H2zM4 7h8l2 7H2z"/></svg>
      <svg viewBox="0 0 16 16" aria-label="Mobile"><path d="M4 1h8v14H4zM5.5 2.5v10h5v-10z"/></svg>
      <svg viewBox="0 0 16 16" aria-label="Fax"><path d="M4 1h8v4H4zM1 6h14v6h-3v3H4v-3H1zM5 10v4h6v-4z"/></svg>
      <svg viewBox="0 0 16 16" aria-label="Email"><path d="M1 3h14v10H1zM2 4.5v.5l6 4 6-4v-.5z"/></svg>
      <svg viewBox="0 0 16 16" aria-label="Address"><path d="M8 1a5 5 0 0 1 5 5c0 4-5 9-5 9S3 10 3 6a5 5 0 0 1 5-5zm0 3a2 2 0 1 0 0 4 2 2 0 0 0 0-4z"/></svg>
    </div>

    <ul class="contact-list">
      <li>07 549 2361</li>
      <li>021 634 915</li>
      <li>07 549 2874</li>
      <li>bond.fix@mailvo.co.nz</li>
      <li>164 Kowhai Lane, Kereru Bay 3175</li>
    </ul>

    <svg class="edge-bands" viewBox="0 0 560 80" aria-hidden="true">
      <path d="M330 80 C 345 55, 350 40, 380 38 L560 38 L560 80 Z" fill="var(--navy)"/>
      <rect x="82" y="62" width="478" height="18" fill="var(--ink)"/>
    </svg>
  </section>

</body>
</html>
```